Lena Hartwell Web

Lena Hartwell is a singer/songwriter that has a presence in the market for over 20 years. She currently has a website, lenahartwell.example that needs a major makeover. IT needs to be reorganized to; 1) make it more user friendly; 2) enable multi-languages including; Spanish, French, Russian, Japanese, Chinese and Portuguese; 3) enable purchases online through a storefront of promotional merchandise and music tracks. She has a logo that needs an update, as well as we currently have a business card open on PixelBazaar for input. Working to re-brand, or refresh her brand.

Lena Hartwell is the next Rosa Delmont! She has 5 platinum records, Lumen Award nominations and tours with Harold Prescott globally and is Nora Vandermeer's key backup singer for 12 years.
Updates

Some common questions have come up.  Here is some further input:

1) Colors - No specific color in mind but probably earth tones.  Although at this point we''re completely open.  Lena likes classical style, Russian, French decor.  Paris architecture. Greek, Italian textures, Goddess like symbols from the Roman Empire, or the symbols and pomp of the British monarchy.  One name on tap for the new CD is "Lanterns Over Quiet Water"
2) Example website - I have not found a new one specifically, but what I don''t like about the existing one is it is not easy to navigate.  Needs to be streamlined and easy to navigate with a storefront for merchandise and music downloads.  
3) On Logo - We''re revamping a "Global" merchandise rollout logo.  We''ve also considered possibly modifying the old english "Hartwell" family crest which signifies royalty, but have not explored that too much.  The hexagon yellow logo on her current website, I was thinking of modifying to gold (brushed - or polished?), then taking the LH lettering using a fountain pen type look there the line thickness flows with pressure on the pen, then make the gold look like a pillow, with the letter making an impression into the gold pillow.  This expands to a high quality pin, blinged up broach with diamonds imbedded for example, Global label identity, tee shirts, label tag on fashion clothing etc etc. 
 4) One thing marketing has asked us to build is a routine video blog to reach out to fans in a personal way.  Short clips of daily activity, travel prep for shows, etc. Possibly a signup/fanpage where people get emails sent back whenever anything new is posted, like a video blog, new pics, new events.  A menu to choose what you get updates on. 

Thanks, Dennis

Target Market(s)

1) Fan base in Europe, Asia, Latin America and North America
2) Movie producers seeking soundtracks
3) Private clients seeking an outstanding performer for corporate events

Industry/Entity Type

Singer

Requirements
Must have
• Better organization into smaller pages. Items critical include: 1) music tracks, 2) ClipStream links, 3) photos & Video, 4) storefront to enable online merchandise purchase 5) a way to illustrate her genre from; gospel, to rock, funk, R&B, country,

```html
<!DOCTYPE html>
<html lang="en">
<head>
<meta charset="utf-8">
<title>Lena Hartwell – About</title>
<link href="https://fonts.googleapis.com/css2?family=Oranienbaum&family=Vollkorn:wght@400&display=swap" rel="stylesheet">
<style>
  :root {
    --page-bg: #221f20;
    --panel-bg: #333232;
    --text-light: #ece8e2;
    --text-body: #e4e0da;
    --link-grey: #d8d4ce;
    --heading-teal: #6aaec8;
    --gold: #b98a3c;
    --band-tan: #dcae70;
    --band-sand: #c9b08a;
    --band-blue: #49b2de;
    --band-ice: #cfeaf4;
  }
  * { margin: 0; padding: 0; box-sizing: border-box; }
  html, body {
    width: 1200px; height: 791px; overflow: hidden;
    background: var(--page-bg);
  }
  .site {
    position: relative; width: 1200px; height: 791px; overflow: hidden;
    background: var(--page-bg);
  }
  .language-bar {
    position: absolute; left: 2px; top: 3px;
    font-family: "Times New Roman", Times, serif;
    font-size: 13.5px; color: #ffffff;
  }
  .language-bar a { color: var(--link-grey); margin-left: 2px; }
  .hero-band {
    position: absolute; left: 0; top: 98px; width: 1200px; height: 168px;
    background:
      repeating-linear-gradient(180deg, rgba(255,255,255,0.18) 0 3px, rgba(255,255,255,0) 3px 11px),
      linear-gradient(90deg, var(--band-tan) 0%, var(--band-tan) 22%, var(--band-sand) 36%, var(--band-ice) 55%, #9fcfe0 68%, var(--band-blue) 86%, var(--band-ice) 100%);
  }
  .sparkle-glow {
    position: absolute; left: 960px; top: 30px; width: 240px; height: 240px;
    background: radial-gradient(circle at 60% 40%, rgba(230,244,250,0.85) 0%, rgba(120,190,225,0.4) 35%, rgba(34,31,32,0) 70%);
  }
  .portrait {
    position: absolute; left: 776px; top: 96px; width: 248px; height: 216px;
    background: linear-gradient(180deg, #1a1718 0%, #4a3528 55%, #6b4a35 100%);
    border-radius: 50% 50% 10% 10% / 40% 40% 5% 5%;
  }
  .brand-name {
    position: absolute; left: 664px; top: 282px;
    font-family: "Vollkorn", Georgia, serif;
    font-size: 60px; line-height: 1; color: var(--gold);
    letter-spacing: 1px;
  }
  .main-nav {
    position: absolute; left: 18px; top: 300px;
    list-style: none;
    font-family: "Oranienbaum", "Times New Roman", serif;
    font-size: 44px; line-height: 36px; color: var(--text-light);
  }
  .main-nav li { height: 36px; }
  .page-title {
    position: absolute; left: 398px; top: 332px;
    font-family: "Oranienbaum", "Times New Roman", serif;
    font-weight: 400; font-size: 52px; line-height: 1;
    color: var(--heading-teal);
  }
  .about-panel {
    position: absolute; left: 397px; top: 397px; width: 722px; height: 420px;
    background: var(--panel-bg);
    padding: 2px 10px 0 10px;
    font-family: "Vollkorn", Georgia, serif;
    font-size: 19.4px; line-height: 24px; color: var(--text-body);
  }
  .about-panel p { margin-bottom: 20px; }
</style>
</head>
<body>
<div class="site">
  <div class="language-bar">Choose your language: <a href="#">English</a> <a href="#">Spanish</a> <a href="#">French</a> <a href="#">Russian</a> <a href="#">Janpanese</a> <a href="#">Chinese</a> <a href="#">Portuguese</a></div>

  <div class="sparkle-glow" role="img" aria-label="Soft glittering sparkle lights"></div>
  <div class="hero-band" role="img" aria-label="Streaked light band fading from warm tan to bright blue"></div>
  <div class="portrait" role="img" aria-label="Portrait photo of the singer in profile"></div>

  <div class="brand-name">Lena Hartwell</div>

  <ul class="main-nav">
    <li>HOME</li>
    <li>ABOUT</li>
    <li>MUSIC</li>
    <li>TOURS</li>
    <li>STORE</li>
    <li>CONTACT</li>
  </ul>

  <h1 class="page-title">About</h1>

  <section class="about-panel">
    <p>Lena Hartwell displays the vocal prowess, attitude and range of a true ingenue. (Chartline Weekly) With a powerfully unique voice and a definitive sound, Lena Hartwell consistently delivers soul stirring performances that captivate audiences around the world. Using her past as a spring board, Lena channels memories into melodies that are proud and strong. Her rich melodic sound and exciting performance style are rooted in the story of a pastor’s daughter with a passion for singing good music.</p>
    <p>With Brightwater Records, Lena began singing for Movie soundtracks and was even featured in the movie Lantern Hall 54 where she portrayed the artist June Caldwell and sang “Tap on the Door” for the soundtrack. She performed “Can’t Look Away From You” with Tony Marchetti for the closing credits of Hidden Agenda. Lena also sang “I Want to Come Back to You” for the movie Full Throttle starring Carl Brennan. Other notable movies that feature Lena’s voice include: Neon Saloon and Target Zero vs Crane. After returning from Europe promoting and shooting the video for “Can’t Go On Without You” by Marco Delvecchio and Sam Porter from Paint It Loud, she was privileged to have</p>
  </section>
</div>
</body>
</html>
```